Tallow Crest Business Card

We need a business card designed for a a company called "Tallow Crest". We offer consulting, coaching and training to business leaders and coaches (across the world) using the latest findings in neuroscience, social and emotional intelligence and positive psychology. The final design should communicate the use of brain science to create sustainable relationships.

The card should be doublesided. The logo is attached and names and titles will be provided to the successful designer. Thank you.

Industry/Entity Type

Training

```html
<!DOCTYPE html>
<html lang="en">
<head>
<meta charset="utf-8">
<title>Tallow Crest Business Card</title>
<link rel="stylesheet" href="https://fonts.googleapis.com/css2?family=Open+Sans:wght@400;600;700&display=swap">
<style>
  :root {
    --backdrop: #e9e6e1;
    --card-black: #0b0b0b;
    --card-white: #ffffff;
    --brand-blue: #1a8ac6;
    --brand-green: #a6ce1b;
    --panel-grey: #6a6a6a;
    --text-dark: #111111;
    --text-light: #ffffff;
  }
  * { margin: 0; padding: 0; box-sizing: border-box; }
  html, body {
    width: 1200px; height: 900px; overflow: hidden;
    background: var(--backdrop);
    font-family: "Open Sans", Arial, sans-serif;
  }
  .canvas {
    position: relative; width: 1200px; height: 900px;
  }
  .card {
    position: absolute; left: 310px; width: 580px; height: 360px;
    overflow: hidden;
    box-shadow: 0 6px 18px rgba(0,0,0,0.18);
  }
  .card--back { top: 70px; background: var(--card-black); }
  .card--front { top: 470px; background: var(--card-white); }

  /* back side */
  .back-brand {
    position: absolute; left: 0; right: 0; top: 118px;
    display: flex; align-items: center; justify-content: center; gap: 14px;
  }
  .brand-dot {
    width: 26px; height: 26px; border-radius: 50%;
    background: var(--brand-green);
  }
  .brand-name {
    font-weight: 700; color: var(--brand-blue); letter-spacing: 1px;
  }
  .back-brand .brand-name { font-size: 44px; }
  .back-web {
    position: absolute; left: 0; right: 0; top: 236px;
    text-align: center; color: var(--text-light);
    font-size: 15px; letter-spacing: 0.5px;
  }

  /* front side */
  .front-shape { position: absolute; inset: 0; }
  .front-brand {
    position: absolute; left: 36px; top: 44px;
    display: flex; align-items: center; gap: 10px;
  }
  .front-brand .brand-dot { width: 18px; height: 18px; }
  .front-brand .brand-name { font-size: 28px; }
  .person {
    position: absolute; left: 36px; top: 228px; color: var(--text-dark);
  }
  .person-name { font-size: 21px; font-weight: 600; }
  .person-title { font-size: 13px; margin-top: 2px; }
  .contact-panel {
    position: absolute; left: 296px; top: 138px; width: 262px; height: 160px;
    background: var(--panel-grey);
    padding: 12px 10px 0 12px;
    color: var(--text-light);
  }
  .contact-list { list-style: none; }
  .contact-list li {
    display: flex; align-items: center; gap: 6px;
    font-size: 12.5px; line-height: 20px; white-space: nowrap;
  }
  .contact-list svg { width: 12px; height: 12px; flex: none; fill: var(--text-light); }
</style>
</head>
<body>
<main class="canvas">

  <section class="card card--back" aria-label="Card back">
    <div class="back-brand">
      <span class="brand-dot"></span>
      <span class="brand-name">Tallow Crest</span>
    </div>
    <p class="back-web">www.tallowcrest-coaching.de</p>
  </section>

  <section class="card card--front" aria-label="Card front">
    <svg class="front-shape" width="580" height="360" viewBox="0 0 580 360" aria-hidden="true">
      <path d="M340 0 Q262 150 256 360 L580 360 L580 0 Z" fill="var(--card-black)"/>
      <path d="M332 0 Q254 150 248 360" fill="none" stroke="var(--brand-green)" stroke-width="7"/>
    </svg>

    <div class="front-brand">
      <span class="brand-dot"></span>
      <span class="brand-name">Tallow Crest</span>
    </div>

    <div class="person">
      <p class="person-name">Marek Dovan</p>
      <p class="person-title">Director</p>
    </div>

    <div class="contact-panel">
      <ul class="contact-list">
        <li><svg viewBox="0 0 12 12"><path d="M6 1 L11 6 H9.5 V11 H7 V8 H5 V11 H2.5 V6 H1 Z"/></svg>Lindenweg 18, 40210 Rheinfeld</li>
        <li><svg viewBox="0 0 12 12"><path d="M1 2.5 H11 V9.5 H1 Z M1.8 3.2 L6 6.5 L10.2 3.2 V8.8 H1.8 Z" fill-rule="evenodd"/></svg>info@tallowcrest-coaching.de</li>
        <li><svg viewBox="0 0 12 12"><path d="M6 1 A5 5 0 1 0 6.01 1 Z M6 2 A4 4 0 1 1 5.99 2 Z M5.5 1.5 H6.5 V10.5 H5.5 Z M1.5 5.5 H10.5 V6.5 H1.5 Z" fill-rule="evenodd"/></svg>www.tallowcrest-coaching.de</li>
        <li><svg viewBox="0 0 12 12"><path d="M1 4 Q6 0 11 4 L10 5.5 L8 4.8 V4 Q6 3.2 4 4 V4.8 L2 5.5 Z M3 6 H9 L10 10 H2 Z"/></svg>0211 / 48 52 17 30</li>
        <li><svg viewBox="0 0 12 12"><path d="M3 1 H8 V4 H3 Z M1 4.5 H11 V10 H1 Z M3 6 H9 V7 H3 Z" fill-rule="evenodd"/></svg>0211 / 48 52 17 39</li>
        <li><svg viewBox="0 0 12 12"><path d="M3.5 0.5 H8.5 V11.5 H3.5 Z M4.3 1.6 H7.7 V7 H4.3 Z" fill-rule="evenodd"/></svg>0151 / 204 36 815</li>
      </ul>
    </div>
  </section>

</main>
</body>
</html>
```